Virtual Racing Community for Runners Needs a Refreshed Web Design

We are a STARTUP. The current website consists of 3 main pages that function well; however, they are not producing the proper conversions because we need a more professional look and better execution of our great ideas.

First page: landing page that needs to be intriguing, sleek, create urgency, incorporate our call to action and most importantly get the consumer to click a button to get to second page. www.trelomark.com

Second page: sign up page that incorporates our already existing postwren form that doesn't take the viewer away from the page on incorrect form field entry. On successful completion needs to inform the viewer to check the email and confirm (possibly in spam) and open third page. http://www.trelomark.com/beta.html

Third page: preorder page that allows the user prepurchase through a well working form through "www.usebaskin.com." This interface works really well; however, the graphics and page need to really entice the viewer to buy. http://www.trelomark.com/preorder.html

And that's it!!! Simple 3 pages that function currently 95% how we want it, but really needs that creative touch to push it to the next level!

Contact us with any other questions!
Updates

Reason: I have provided numerous feedback and am awaiting redesigns. Have it narrowed down to 2 designers. Need time to vet with stakeholders.

Industry/Entity Type

Racing

```html
<!DOCTYPE html>
<html lang="en">
<head>
<meta charset="utf-8">
<title>Trelomark — Motivate Yourself to Race</title>
<link href="https://fonts.googleapis.com/css2?family=League+Gothic&display=swap" rel="stylesheet">
<style>
:root{
  --red:#b71f18;
  --red-dark:#9b1b14;
  --brown:#8c3a12;
  --blue:#5897b3;
  --blue-band:#5599b5;
  --ink:#111;
  --footer:#141414;
  --text:#333;
  --muted:#555;
  --pink:#f7d2cd;
  --white:#fff;
}
*{margin:0;padding:0;box-sizing:border-box}
html,body{width:1200px;height:1053px;overflow:hidden;background:var(--white)}
body{position:relative;font-family:Arial,Helvetica,sans-serif;color:var(--text)}
.display{font-family:"League Gothic",Impact,sans-serif;font-weight:400;text-transform:uppercase;line-height:1}

.hero-photo{position:absolute;left:0;top:0;width:1200px;height:522px;
  background:
    radial-gradient(ellipse 420px 300px at 300px 280px,rgba(232,196,168,.95),rgba(232,196,168,0) 70%),
    linear-gradient(180deg,rgba(255,255,255,0) 60%,rgba(188,70,50,.9) 75%,#a8402e 100%),
    linear-gradient(90deg,#5f8a3c 0%,#d9c8a8 25%,#d2d8d8 50%,#9cc4e0 70%,#4a8fc8 100%);}
.hero-photo::after{content:"";position:absolute;left:560px;top:180px;width:640px;height:200px;
  background:linear-gradient(180deg,rgba(120,160,70,0),rgba(110,150,60,.55),rgba(120,160,70,0))}

.brand{position:absolute;left:607px;top:22px;font-size:100px;color:var(--ink);letter-spacing:2px}
.headline{position:absolute;left:605px;top:141px;font-size:56px;color:var(--red-dark)}
.tagline{position:absolute;left:605px;top:195px;font-size:42px;color:var(--red-dark);letter-spacing:2px}
.event-title{position:absolute;left:605px;top:281px;font-size:42px;color:var(--ink)}
.event-copy{position:absolute;left:608px;top:325px;width:380px;font-size:14px;line-height:16px;color:var(--ink)}
.cta{position:absolute;left:604px;top:375px;width:254px;height:54px;display:flex}
.cta-arrow{width:61px;background:var(--ink);display:flex;align-items:center;justify-content:center}
.cta-label{flex:1;background:var(--red);color:var(--pink);font-size:36px;display:flex;align-items:center;justify-content:center;padding-top:2px}

.news{position:absolute;left:110px;top:486px;width:980px;height:104px;background:var(--red);display:flex}
.news-date{width:98px;background:var(--blue);color:var(--white);text-align:center;padding-top:17px}
.news-day{width:42px;height:42px;margin:0 auto;border:2px solid var(--white);border-radius:50%;font-size:22px;line-height:38px}
.news-month{font-size:14px;margin-top:9px}
.news-body{padding:15px 16px;color:var(--white)}
.news-title{font-size:17px;margin-bottom:11px}
.news-text{font-size:12.5px;line-height:16px}

.features{position:absolute;left:110px;top:590px;width:980px;height:212px;background:var(--white);box-shadow:0 14px 22px rgba(0,0,0,.08)}
.feature{position:absolute;top:68px;width:250px}
.feature-icon{position:absolute;left:-60px;top:2px}
.feature-title{font-size:18px;color:var(--text);margin-bottom:6px}
.feature-text{font-size:12.5px;line-height:16px;color:var(--muted);height:48px}
.view-btn{display:flex;margin-top:6px;height:25px;width:77px}
.view-label{width:49px;background:var(--brown);color:var(--white);font-size:12px;display:flex;align-items:center;justify-content:center}
.view-arrow{flex:1;background:var(--ink);display:flex;align-items:center;justify-content:center}

.footer{position:absolute;left:0;top:862px;width:1200px;height:128px;background:var(--footer);color:var(--white)}
.connect-title{position:absolute;left:113px;top:30px;font-size:28px;letter-spacing:1px}
.social{position:absolute;left:115px;top:72px;display:flex;gap:20px}
.social span{width:40px;height:40px;border:2px solid var(--white);border-radius:50%}
.contact{position:absolute;left:829px;top:32px}
.contact-row{display:flex;align-items:center;gap:12px}
.contact-address{font-size:12px;line-height:18px;color:#ddd}
.contact-phone{font-size:24px;color:#ccc;margin-top:8px}
.bottom-band{position:absolute;left:0;top:990px;width:1200px;height:48px;background:var(--blue-band);color:var(--white);font-size:11px}
.copyright{position:absolute;left:115px;top:18px}
.legal{position:absolute;right:115px;top:18px}
.base-strip{position:absolute;left:0;top:1038px;width:1200px;height:15px;background:var(--footer)}
</style>
</head>
<body>

<div class="hero-photo" role="img" aria-label="Runner kneeling on a red running track tying the laces of a white and blue running shoe, green field and blue sky behind"></div>

<div class="brand display">Trelomark</div>
<h1 class="headline display">Motivate yourself to race</h1>
<div class="tagline display">Challenge. Commit. Change.</div>
<h2 class="event-title display">Chicago Beta Run Week 2</h2>
<p class="event-copy">For a limited time be the first to receive early access and receive a Real Life Beta Tester t-shirt.</p>
<a class="cta">
  <span class="cta-arrow"><svg width="24" height="20" viewBox="0 0 24 20"><path d="M2 10H20M12 2l8 8-8 8" stroke="#fff" stroke-width="3" fill="none"/></svg></span>
  <span class="cta-label display">Register now</span>
</a>

<section class="news">
  <div class="news-date">
    <div class="news-day">23</div>
    <div class="news-month">AUG</div>
  </div>
  <div class="news-body">
    <div class="news-title">Latest Virtual Run</div>
    <p class="news-text">Lorem ipsum dolor sit amet, consectetur adipisicing elit, sed do eiusmod tempor incididunt ut labore et dolore magna aliqua. Ut enim ad minim veniam, quis nostrud exercitation ullamco laboris nisi ut aliquip ex ea commodo consequat.</p>
  </div>
</section>

<section class="features">
  <div class="feature" style="left:84px">
    <svg class="feature-icon" width="42" height="42" viewBox="0 0 42 42"><path d="M11 3h20v12a10 10 0 0 1-20 0z" fill="#333"/><path d="M11 7H4v4a8 8 0 0 0 8 8M31 7h7v4a8 8 0 0 1-8 8" stroke="#333" stroke-width="3" fill="none"/><rect x="18" y="24" width="6" height="8" fill="#333"/><rect x="12" y="32" width="18" height="7" fill="#333"/></svg>
    <div class="feature-title">freebies and giveaways</div>
    <p class="feature-text">Duis aute irure dolor in reprehenderit in voluptate velit esse cillum dolore eu fugiat nulla pariatur.</p>
    <a class="view-btn"><span class="view-label">view</span><span class="view-arrow"><svg width="12" height="10" viewBox="0 0 12 10"><path d="M1 5h9M6 1l4 4-4 4" stroke="#fff" stroke-width="1.6" fill="none"/></svg></span></a>
  </div>
  <div class="feature" style="left:407px">
    <svg class="feature-icon" width="44" height="46" viewBox="0 0 44 46"><circle cx="22" cy="26" r="16" stroke="#333" stroke-width="4" fill="none"/><rect x="18" y="2" width="8" height="5" fill="#333"/><path d="M22 26V16" stroke="#333" stroke-width="3"/><path d="M35 10l4-4" stroke="#333" stroke-width="3"/></svg>
    <div class="feature-title">run at your own pace</div>
    <p class="feature-text">You can walk, jog, skip or run the distance of your choice. You can complete your race at the gym ...</p>
    <a class="view-btn"><span class="view-label">view</span><span class="view-arrow"><svg width="12" height="10" viewBox="0 0 12 10"><path d="M1 5h9M6 1l4 4-4 4" stroke="#fff" stroke-width="1.6" fill="none"/></svg></span></a>
  </div>
  <div class="feature" style="left:735px">
    <svg class="feature-icon" width="52" height="48" viewBox="0 0 52 48" style="left:-68px;top:-2px"><circle cx="18" cy="12" r="9" stroke="#333" stroke-width="3" fill="#fff"/><circle cx="38" cy="22" r="11" fill="#333"/><circle cx="17" cy="32" r="13" stroke="#333" stroke-width="4" fill="#fff"/><text x="17" y="38" font-size="16" font-family="Arial" font-weight="700" text-anchor="middle" fill="#333">$</text><text x="38" y="27" font-size="13" font-family="Arial" font-weight="700" text-anchor="middle" fill="#fff">$</text><text x="18" y="16" font-size="10" font-family="Arial" font-weight="700" text-anchor="middle" fill="#333">$</text></svg>
    <div class="feature-title">discounts</div>
    <p class="feature-text">If you have 10 or more runners interested in participating in one of our races, please contact us and ...</p>
    <a class="view-btn"><span class="view-label">view</span><span class="view-arrow"><svg width="12" height="10" viewBox="0 0 12 10"><path d="M1 5h9M6 1l4 4-4 4" stroke="#fff" stroke-width="1.6" fill="none"/></svg></span></a>
  </div>
</section>

<footer class="footer">
  <div class="connect-title display">Connect with us</div>
  <div class="social" aria-label="Social network links"><span></span><span></span><span></span><span></span></div>
  <div class="contact">
    <div class="contact-row">
      <svg width="34" height="34" viewBox="0 0 34 34"><circle cx="17" cy="17" r="15.5" stroke="#fff" stroke-width="2" fill="none"/><path d="M8 17l9-8 9 8h-3v7h-4v-5h-4v5h-4v-7z" fill="#fff"/></svg>
      <div class="contact-address">580 Larkfield Road Suite 14<br>Eastbrook, Ohio 443210</div>
    </div>
    <div class="contact-row contact-phone">
      <svg width="34" height="34" viewBox="0 0 34 34"><circle cx="17" cy="17" r="15.5" stroke="#fff" stroke-width="2" fill="none"/><path d="M12 9c-2 1-3 3-2 6 2 5 5 8 9 10 3 1 5 0 6-2l-3-3-2 2c-2-1-4-3-5-5l2-2z" fill="#fff"/></svg>
      <span>555-014-2286</span>
    </div>
  </div>
</footer>

<div class="bottom-band">
  <div class="copyright">© Copyright 2014 Trelomark. All Rights Reserved</div>
  <div class="legal">Policy | Terms</div>
</div>
<div class="base-strip"></div>

</body>
</html>
```